Wordpress template re-design of current website

We need a WordPress template design and new look for our existing website. Our existing site it located at www.velmoro.com.au We are a tech company and want a fresh, clean modern website that matches our brand, services and logo colors. Our main Services are hospitality solutions, Velmoro TV solution and managed networks, more information on these can come from our existing website.

Target Market(s)

We are a tech company so must have a modern feel for new technology

Industry/Entity Type

It Company

Number of Pages Required

5+ page

Font styles to use
Sans Serif

Requirements
Must have
• Be based on a wordpress templete design and match the services that we have in our existing website, in the testimonials want a place for video testimonials as well as text. Nice clean icons used for graphics to represent services.
Nice to have
• nice visual representation of our services in the way of clean icons etc
Should not have
• Clutter

```html
<!DOCTYPE html>
<html lang="en">
<head>
<meta charset="utf-8">
<title>Velmoro Wireless – Services</title>
<link rel="stylesheet" href="https://fonts.googleapis.com/css2?family=Roboto+Condensed:wght@400;700&family=Open+Sans:wght@400;600&family=Roboto:wght@300;400&display=swap">
<style>
:root{
  --brand:#0d4a8f;
  --brand-dark:#0b3d78;
  --hero:#2a68ad;
  --ink:#333;
  --muted:#555;
  --light:#f6f7f9;
  --band:#1e1e1e;
  --bottom:#2b2b2b;
  --white:#fff;
}
*{margin:0;padding:0;box-sizing:border-box}
html,body{width:759px;height:1200px;overflow:hidden;background:var(--white)}
body{position:relative;font-family:'Open Sans',sans-serif;color:var(--ink)}
.abs{position:absolute}

/* header */
.site-header{left:0;top:0;width:759px;height:62px;border-top:2px solid var(--brand);background:var(--white)}
.brand{left:63px;top:18px;font-family:'Roboto',sans-serif;font-size:24px;font-weight:400;color:var(--brand);display:flex;align-items:center;gap:6px}
.brand-dot{width:12px;height:12px;border-radius:50%;background:var(--brand)}
.main-nav{left:242px;top:21px;display:flex;font-family:'Roboto Condensed',sans-serif;font-size:9px;color:#444}
.main-nav span{padding:5px 13px;border:1px solid transparent;border-radius:3px;margin-right:4px}
.main-nav .active{border-color:var(--brand);color:var(--brand)}
.header-contact{left:565px;top:0;width:194px;height:62px;border-left:1px solid #eee}
.header-contact .lines{position:absolute;right:91px;top:19px;text-align:right;font-size:8px;line-height:12px;color:#333;white-space:nowrap}
.header-contact .lines b{font-weight:400;font-size:9px}
.phone-circle{position:absolute;left:111px;top:20px;width:21px;height:21px;border:1px solid var(--brand);border-radius:50%}

/* hero */
.page-hero{left:0;top:62px;width:759px;height:112px;background:linear-gradient(180deg,#3a79bf,#1f5aa0)}
.page-hero h1{position:absolute;left:0;right:0;top:44px;text-align:center;font-family:'Roboto Condensed',sans-serif;font-weight:700;font-size:30px;color:var(--white);letter-spacing:.5px}

/* overview */
.overview-image{left:62px;top:206px;width:249px;height:153px;background:radial-gradient(circle at 50% 45%,#bfe4ff,#2f8ad8 45%,#0d4f9e)}
.overview-title{left:334px;top:203px;font-family:'Roboto Condensed',sans-serif;font-weight:400;font-size:20px;color:var(--brand)}
.overview-text{left:335px;top:233px;width:363px;font-size:7px;line-height:14px;color:var(--muted)}
.overview-text p+p{margin-top:9px}

/* services */
.services{left:0;top:394px;width:759px;height:341px;background:var(--light);border-top:1px solid #eee}
.service{position:absolute;width:300px}
.service-icon{position:absolute;left:0;top:0;width:54px;height:54px;border-radius:50%;background:var(--brand);display:flex;align-items:center;justify-content:center}
.service-icon::after{content:"";position:absolute;left:4px;top:62px;width:46px;height:4px;border-radius:50%;background:rgba(0,0,0,.06)}
.service h3{position:absolute;left:72px;top:1px;font-family:'Roboto',sans-serif;font-weight:300;font-size:12.5px;color:#333;white-space:nowrap}
.service p{position:absolute;left:72px;top:24px;width:231px;font-size:6.6px;line-height:13px;color:var(--muted)}
.service a{position:absolute;left:72px;top:124px;font-size:7.5px;color:var(--brand);text-decoration:underline}

/* band */
.statement{left:0;top:735px;width:759px;height:201px;background:linear-gradient(180deg,#2a2a2a,#111);text-align:center;color:var(--white)}
.statement h2{position:absolute;left:0;right:0;top:52px;font-family:'Roboto Condensed',sans-serif;font-weight:700;font-size:31px}
.statement p{position:absolute;left:0;right:0;top:94px;font-family:'Roboto',sans-serif;font-size:15.5px;line-height:20px}

/* partners */
.partner{top:958px;width:97px;height:46px;border:1px solid #e2e2e2;background:var(--white)}
.partner i{position:absolute;left:24px;top:15px;width:49px;height:16px;border-radius:3px;background:#d9dde3}

/* footer */
.site-footer{left:0;top:1022px;width:759px;height:144px;background:linear-gradient(180deg,#0e4a8c,#0a3a72);color:var(--white)}
.footer-brand{left:64px;top:46px;font-family:'Roboto',sans-serif;font-size:24px;display:flex;align-items:center;gap:6px}
.footer-brand .brand-dot{background:var(--white)}
.socials{left:72px;top:87px;display:flex;gap:4px}
.socials i{width:15px;height:15px;border:1px solid var(--white);border-radius:50%}
.foot-h{font-family:'Roboto',sans-serif;font-size:11px;top:25px;white-space:nowrap}
.quick-links{left:208px;top:53px;font-size:7px;line-height:15.2px}
.contact-list{left:326px;top:53px;font-size:7.5px;color:var(--white)}
.contact-list .row{position:absolute;left:0;display:flex;gap:10px;white-space:nowrap;line-height:12px}
.field{left:526px;width:171px;height:28px;border:1px solid #2d64a3;font-size:7px;padding:9px 9px;color:#dde}
.subscribe{left:635px;top:1108px;width:62px;height:25px;background:#1c1c1c;color:var(--white);font-size:8px;text-align:center;line-height:25px}
.copyright{left:0;top:1166px;width:759px;height:34px;background:var(--bottom);color:#ddd;font-size:7.5px;text-align:center;line-height:34px}
</style>
</head>
<body>

<header class="abs site-header">
  <div class="abs brand"><span>Velmoro</span><span class="brand-dot"></span></div>
  <nav class="abs main-nav">
    <span>HOME</span><span>ABOUT US</span><span class="active">SERVICES</span><span>OUR WORK</span><span>CONTACT</span>
  </nav>
  <div class="abs header-contact">
    <div class="lines"><b>+1 1300 555 014</b><br>info@velmoro.com.au</div>
    <div class="phone-circle">
      <svg width="19" height="19" viewBox="0 0 21 21"><path d="M7 6c1 0 1.5 2 1.3 2.6L7.6 9.4c.6 1.5 1.9 2.8 3.4 3.4l.8-.7c.6-.2 2.6.3 2.6 1.3 0 1-1 1.6-1.8 1.6C9.3 15 5.4 11.1 5.4 7.8 5.4 7 6 6 7 6z" fill="#0d4a8f"/></svg>
    </div>
  </div>
</header>

<section class="abs page-hero"><h1>SERVICES</h1></section>

<div class="abs overview-image" role="img" aria-label="Connected laptops and devices networked over a world map"></div>
<h2 class="abs overview-title">SERVICES OVERVIEW</h2>
<div class="abs overview-text">
  <p>Lorem ipsum dolor sit amet, consectetur adipiscing elit, sed do eiusmod tempor incididunt ut labore et dolore magna aliqua. Ut enim ad minim veniam, quis nostrud exercitation ullamco laboris nisi ut aliquip ex ea commodo consequat. Duis aute irure dolor in reprehenderit in voluptate velit esse cillum dolore eu fugiat nulla pariatur. Excepteur sint occaecat cupidatat non proident, sunt in culpa qui officia deserunt mollit anim id est laborum</p>
  <p>Lorem ipsum dolor sit amet, consectetur adipiscing elit, sed do eiusmod tempor incididunt ut labore et dolore magna aliqua. Ut enim ad minim veniam, quis nostrud exercitation ullamco laboris nisi ut aliquip ex ea commodo consequat. Duis aute irure dolor in reprehenderit</p>
</div>

<section class="abs services">
  <article class="service" style="left:62px;top:22px">
    <div class="service-icon"><svg width="24" height="24" viewBox="0 0 24 24"><rect x="7" y="2" width="10" height="20" rx="2" fill="none" stroke="#fff" stroke-width="2"/><circle cx="12" cy="18.5" r="1.1" fill="#fff"/></svg></div>
    <h3>Hospitality Solutions</h3>
    <p>Lorem ipsum dolor sit amet, consectetur adipiscing elit, sed do eiusmod tempor incididunt ut labore et dolore magna aliqua. Ut enim ad minim veniam, quis nostrud exercitation ullamco laboris nisi ut aliquip ex ea commodo consequat. Duis aute irure dolor in reprehenderit in voluptate velit esse cillum dolore eu fugiat nulla pariatur. Excepteur sint occaecat cupidatat non proident, sunt in culpa qui officia deserunt mollit anim id est laborum</p>
    <a>Read More</a>
  </article>
  <article class="service" style="left:396px;top:22px">
    <div class="service-icon"><svg width="26" height="24" viewBox="0 0 26 24"><rect x="2" y="6" width="22" height="15" rx="2" fill="none" stroke="#fff" stroke-width="2"/><path d="M9 6V3h8v3" fill="none" stroke="#fff" stroke-width="2"/><path d="M13 9.5v8M9 13.5h8" stroke="#fff" stroke-width="2.4"/></svg></div>
    <h3>Mobile Solutions</h3>
    <p>Lorem ipsum dolor sit amet, consectetur adipiscing elit, sed do eiusmod tempor incididunt ut labore et dolore magna aliqua. Ut enim ad minim veniam, quis nostrud exercitation ullamco laboris nisi ut aliquip ex ea commodo consequat. Duis aute irure dolor in reprehenderit in voluptate velit esse cillum dolore eu fugiat nulla pariatur. Excepteur sint occaecat cupidatat non proident, sunt in culpa qui officia deserunt mollit anim id est laborum</p>
    <a>Read More</a>
  </article>
  <article class="service" style="left:62px;top:190px">
    <div class="service-icon"><svg width="26" height="24" viewBox="0 0 26 24"><rect x="2" y="3" width="22" height="14" rx="1.5" fill="none" stroke="#fff" stroke-width="2.2"/><path d="M10 21h6M13 17v4" stroke="#fff" stroke-width="2.2"/></svg></div>
    <h3>Mining and Remote</h3>
    <p>Lorem ipsum dolor sit amet, consectetur adipiscing elit, sed do eiusmod tempor incididunt ut labore et dolore magna aliqua. Ut enim ad minim veniam, quis nostrud exercitation ullamco laboris nisi ut aliquip ex ea commodo consequat. Duis aute irure dolor in reprehenderit in voluptate velit esse cillum dolore eu fugiat nulla pariatur. Excepteur sint occaecat cupidatat non proident, sunt in culpa qui officia deserunt mollit anim id est laborum</p>
    <a>Read More</a>
  </article>
  <article class="service" style="left:396px;top:190px">
    <div class="service-icon"><svg width="26" height="22" viewBox="0 0 26 22"><path d="M2 8a16 16 0 0 1 22 0M5.5 11.5a11 11 0 0 1 15 0M9 15a6 6 0 0 1 8 0" fill="none" stroke="#fff" stroke-width="2.2" stroke-linecap="round"/><circle cx="13" cy="18.5" r="1.8" fill="#fff"/></svg></div>
    <h3>Social Wi-Fi</h3>
    <p>Lorem ipsum dolor sit amet, consectetur adipiscing elit, sed do eiusmod tempor incididunt ut labore et dolore magna aliqua. Ut enim ad minim veniam, quis nostrud exercitation ullamco laboris nisi ut aliquip ex ea commodo consequat. Duis aute irure dolor in reprehenderit in voluptate velit esse cillum dolore eu fugiat nulla pariatur. Excepteur sint occaecat cupidatat non proident, sunt in culpa qui officia deserunt mollit anim id est laborum</p>
    <a>Read More</a>
  </article>
</section>

<section class="abs statement" role="img" aria-label="Dark background of a person working on a laptop">
  <h2>VELMORO WIRELESS</h2>
  <p>has been a leader in wireless<br>networks and internet billing systems for over a decade.</p>
</section>

<div class="abs partner" style="left:61px"><i></i></div>
<div class="abs partner" style="left:169px"><i></i></div>
<div class="abs partner" style="left:277px"><i></i></div>
<div class="abs partner" style="left:384px"><i></i></div>
<div class="abs partner" style="left:492px"><i></i></div>
<div class="abs partner" style="left:599px"><i></i></div>

<footer class="abs site-footer">
  <div class="abs footer-brand"><span>Velmoro</span><span class="brand-dot"></span></div>
  <div class="abs socials"><i></i><i></i><i></i><i></i></div>

  <div class="abs foot-h" style="left:208px">QUICK LINKS</div>
  <div class="abs quick-links">CASE STUDIES<br>TESTIMONIALS<br>NEWS<br>RESELLERS</div>

  <div class="abs foot-h" style="left:326px">CONTACT US</div>
  <div class="abs contact-list">
    <div class="row" style="top:4px"><svg width="8" height="11" viewBox="0 0 8 11"><path d="M4 0a4 4 0 0 1 4 4c0 3-4 7-4 7S0 7 0 4a4 4 0 0 1 4-4z" fill="#fff"/><circle cx="4" cy="4" r="1.4" fill="#0d4a8f"/></svg><span><b style="font-weight:600">Velmoro Wireless</b> 42 Harbour Crescent<br>Coral Bay, QLD 4220</span></div>
    <div class="row" style="top:35px;font-size:10px"><svg width="9" height="9" viewBox="0 0 9 9"><path d="M2 0c1 0 1.5 1.8 1.3 2.3L2.7 3c.6 1.3 1.6 2.3 2.9 2.9l.7-.6C6.8 5.1 9 5.6 9 6.6 9 7.6 8 9 7 9 3.3 9 0 5.7 0 2 0 1 1 0 2 0z" fill="#fff"/></svg><span>1300 555 014</span></div>
    <div class="row" style="top:56px"><svg width="10" height="8" viewBox="0 0 10 8"><rect x=".5" y=".5" width="9" height="7" fill="none" stroke="#fff"/><path d="M.5.5 5 4.5 9.5.5" fill="none" stroke="#fff"/></svg><span>sales@velmoro.com.au</span></div>
  </div>

  <div class="abs foot-h" style="left:526px;top:24px">SIGN UP TO RECEIVE EMAIL</div>
</footer>
<div class="abs field" style="top:1074px">Enter Name</div>
<div class="abs field" style="top:1107px">Enter Email</div>
<div class="abs subscribe">SUBSCRIBE</div>

<div class="abs copyright">© 2015 Velmoro Wireless. All Rights Reserved.</div>

</body>
</html>
```